Online Certificate in Research Methods needs a Digital Banner ad

We are launching an online graduate certificate in Quantitative and Qualitative Social Science Research Methods. We need a digital banner created so we can advertise on pagenook, seekora, and some other places.

The banner needs to use these color schemes and fonts: https://universityrelations.bmlu.edu/brand-guide/color

Would like the banner to say (either as three lines, or if not in three lines, have these sets of words at minimum on the same line):
Online Graduate Certificate in
Quantitative & Qualitative
Social Science Research Methods

We also want it to say Brennmoor Lake University and Next Start Date August 18, 2021. I’ve attached a picture of a version we tried to create but is hard to read.

We need a graphic that looks good in the following specs:
600px wide x 70px tall, high quality (at least 300 dpi) jpg or png

And
Pagenook recommendations:
Design Recommendations
• File Type: JPG or PNG
• Ratio: 1.91:1 to 1:1
• Resolution: At least 1080 x 1080 pixels
Text Recommendations
• Primary Text: 125 characters
• Headline: 40 characters
• Description: 30 characters
Technical Requirements
• Maximum File Size: 30MB
• Minimum Width: 600 pixels
• Minimum Height: 600 pixels
• Aspect Ratio Tolerance: 3%

```html
<!DOCTYPE html>
<html lang="en">
<head>
<meta charset="utf-8">
<title>Brennmoor Lake University – Online Graduate Certificate</title>
<link rel="stylesheet" href="https://fonts.googleapis.com/css2?family=Outfit:wght@400;600;700&family=Questrial&display=swap">
<style>
  :root {
    --navy: #002855;
    --gold: #eaaa00;
    --white: #ffffff;
    --photo-warm: #8a5a34;
    --photo-cool: #2f8a7e;
  }
  * { margin: 0; padding: 0; box-sizing: border-box; }
  html, body { width: 1200px; height: 1200px; overflow: hidden; background: var(--navy); }
  .banner {
    position: relative;
    width: 1200px;
    height: 1200px;
    background: var(--navy);
    font-family: "Outfit", sans-serif;
    color: var(--white);
    overflow: hidden;
  }
  .banner__shapes { position: absolute; inset: 0; }
  .brand {
    position: absolute;
    left: 47px;
    top: 56px;
    display: flex;
    align-items: center;
    gap: 16px;
  }
  .brand__mark { width: 94px; height: 94px; background: var(--gold); }
  .brand__name {
    font-family: "Outfit", sans-serif;
    font-weight: 400;
    font-size: 46px;
    color: var(--white);
    white-space: nowrap;
  }
  .accent-rule {
    position: absolute;
    left: 20px;
    top: 253px;
    width: 10px;
    height: 781px;
    background: var(--gold);
  }
  .headline {
    position: absolute;
    left: 63px;
    top: 258px;
    font-weight: 600;
    font-size: 94px;
    line-height: 111px;
    letter-spacing: -0.5px;
  }
  .program {
    position: absolute;
    left: 72px;
    top: 690px;
    font-family: "Questrial", sans-serif;
    font-size: 54px;
    line-height: 62px;
  }
  .start-date {
    position: absolute;
    left: 53px;
    top: 1058px;
    font-weight: 600;
    font-size: 47px;
    color: var(--navy);
    white-space: nowrap;
    letter-spacing: -0.5px;
  }
  .cta {
    position: absolute;
    left: 924px;
    top: 1062px;
    font-weight: 700;
    font-size: 40px;
    color: var(--navy);
    letter-spacing: 1px;
    white-space: nowrap;
  }
</style>
</head>
<body>
<main class="banner">
  <svg class="banner__shapes" width="1200" height="1200" viewBox="0 0 1200 1200" aria-hidden="false">
    <defs>
      <linearGradient id="photo-tones" x1="0" y1="0" x2="1" y2="1">
        <stop offset="0" stop-color="var(--photo-warm)"/>
        <stop offset="0.55" stop-color="#b98a6a"/>
        <stop offset="1" stop-color="var(--photo-cool)"/>
      </linearGradient>
    </defs>
    <polygon class="photo-frame" points="950,57 1200,57 1200,950 950,950 627,503" fill="var(--gold)"/>
    <polygon class="photo-area" role="img" aria-label="Photo of a smiling student holding red folders, wearing a backpack and headphones" points="981,95 1200,95 1200,907 981,907 699,502" fill="url(#photo-tones)"/>
    <polygon class="info-band" points="0,1034 733,1034 839,1132 0,1132" fill="var(--white)"/>
    <polygon class="cta-band" points="789,1034 1200,1034 1200,1132 897,1132" fill="var(--white)"/>
  </svg>

  <div class="brand">
    <span class="brand__mark" aria-hidden="true"></span>
    <span class="brand__name">Brennmoor Lake University</span>
  </div>

  <div class="accent-rule"></div>

  <h1 class="headline">Online<br>Graduate<br>Certificate</h1>

  <p class="program">Quantitative &amp; Qualitative<br>Social Science Research<br>Methods</p>

  <p class="start-date">Next Start Date August 18, 2021</p>
  <p class="cta">LEARN MORE</p>
</main>
</body>
</html>
```